Sunny Doodles - Face Painting Company requires business card design

Hi,
I am wanting a business card design for a new business in Brisbane (Australia) called 'Sunny Doodles'. We are a childrens face painting company.

I want to communicate a corporate, simple and clean message through my business card, but also fun and relevant to children.

My company colours are black, yellow and purple, and at the moment I am running with a "cheeky smile" type theme, along the lines of the Marlow Fox (Tobin and the Glass Kite).

I want this to look Corporate, clean and simple. On the back I would like to see some creative flair with a border or background design, perhaps in white or another colour.

• Front:
Sunny Doodles
Face Painting Designs

Back:
Hana Melrose
Artist
0432 918 246
hana@sunnydoodles.com.au
www.sunnydoodles.com.au
• Attached is the banner which i had made, the business card should go along with this type of theme.
I would like to use the colours Yellow, Black and Purple. Purple should be used in a miniml way, with yellow and black as the main colours.
I want it to have a CORPORATE look.

A Playfull but readable text.

I would like a mix up of the colours on the back in the text.
Hana Melrose (black)
Artist(purple) etc.

```html
<!DOCTYPE html>
<html lang="en">
<head>
<meta charset="utf-8">
<title>Sunny Doodles – Business Cards</title>
<link rel="stylesheet" href="https://fonts.googleapis.com/css2?family=Josefin+Sans:wght@400;600;700&family=Kaushan+Script&display=swap">
<style>
  :root {
    --sun-yellow: #f3ea4f;
    --ink-black: #111111;
    --grape-purple: #7d3f98;
    --paper-white: #ffffff;
    --backdrop: #e9e6df;
    --soft-grey: #d9d9d9;
    --card-shadow: rgba(0, 0, 0, 0.28);
  }
  * { box-sizing: border-box; margin: 0; padding: 0; }
  html, body {
    width: 1200px; height: 771px; overflow: hidden;
    background: var(--backdrop);
    font-family: "Josefin Sans", "Century Gothic", sans-serif;
  }
  .sheet { position: relative; width: 1200px; height: 771px; }
  .card {
    position: absolute; width: 493px; height: 301px; overflow: hidden;
    box-shadow: 6px 8px 10px var(--card-shadow);
  }
  .card--front { background: var(--sun-yellow); }
  .card--back { background: var(--paper-white); }
  .pos-a { left: 61px;  top: 48px; }
  .pos-b { left: 655px; top: 48px; }
  .pos-c { left: 61px;  top: 427px; }
  .pos-d { left: 655px; top: 427px; }

  .art { position: absolute; display: block; }
  .brand-name {
    position: absolute; left: 0; right: 0; text-align: center;
    font-family: "Josefin Sans", sans-serif; font-weight: 700;
    color: var(--ink-black); text-transform: uppercase; letter-spacing: 1px;
  }
  .tagline {
    position: absolute; left: 0; right: 0; text-align: center;
    color: var(--grape-purple);
  }
  .tagline--plain { font-family: "Josefin Sans", sans-serif; font-weight: 400; font-size: 29px; }
  .tagline--script { font-family: "Kaushan Script", cursive; font-size: 30px; }

  .artist-name {
    position: absolute; left: 0; right: 0; text-align: center;
    font-family: "Josefin Sans", sans-serif; font-weight: 400;
    font-size: 54px; color: var(--ink-black); top: 92px;
  }
  .artist-role {
    position: absolute; left: 0; right: 0; text-align: center;
    font-family: "Kaushan Script", cursive; font-size: 40px;
    color: var(--grape-purple); top: 146px;
  }
  .contact-bar {
    position: absolute; left: 0; right: 0; bottom: 0; height: 50px;
    display: flex; align-items: center; justify-content: center; gap: 7px;
    font-size: 14.5px; padding-top: 3px;
  }
  .contact-bar--purple { background: var(--grape-purple); color: var(--paper-white); }
  .contact-bar--yellow { background: var(--sun-yellow); color: var(--ink-black); font-weight: 600; }
  .dot { width: 4px; height: 4px; border-radius: 50%; display: inline-block; margin-top: -3px; }
  .contact-bar--purple .dot { background: var(--sun-yellow); }
  .contact-bar--yellow .dot { background: var(--grape-purple); }
</style>
</head>
<body>
<main class="sheet">

  <!-- Front, version one -->
  <section class="card card--front pos-a">
    <svg class="art" style="left:139px; top:22px;" width="214" height="138" role="img" aria-label="Illustration of two smiling cartoon children with painted cheeks">
      <defs>
        <radialGradient id="kidsTone" cx="50%" cy="50%" r="55%">
          <stop offset="0%" stop-color="#e8dc3e"/>
          <stop offset="100%" stop-color="#f3ea4f"/>
        </radialGradient>
      </defs>
      <rect width="214" height="138" rx="20" fill="url(#kidsTone)"/>
    </svg>
    <div class="brand-name" style="top:180px; font-size:52px;">Sunny Doodles</div>
    <div class="tagline tagline--plain" style="top:247px;">Face Painting Designs</div>
  </section>

  <!-- Front, version two -->
  <section class="card card--front pos-b">
    <svg class="art" style="left:230px; top:0;" width="263" height="301" role="img" aria-label="Decorative white swirl pattern">
      <defs>
        <linearGradient id="swirlTone" x1="0" y1="0" x2="1" y2="1">
          <stop offset="0%" stop-color="#ffffff" stop-opacity="0"/>
          <stop offset="100%" stop-color="#ffffff" stop-opacity="0.55"/>
        </linearGradient>
      </defs>
      <rect width="263" height="301" fill="url(#swirlTone)"/>
    </svg>
    <svg class="art" style="left:145px; top:24px;" width="206" height="90" role="img" aria-label="Illustration of a wide cheeky grin">
      <rect width="206" height="90" rx="40" fill="#fbf6b8"/>
    </svg>
    <div class="brand-name" style="top:143px; font-size:52px;">Sunny Doodles</div>
    <div class="tagline tagline--script" style="top:206px;">Face Painting Designs</div>
  </section>

  <!-- Back, version one -->
  <section class="card card--back pos-c">
    <svg class="art" style="left:139px; top:166px;" width="180" height="78" role="img" aria-label="Faint illustration of a wide cheeky grin">
      <rect width="180" height="78" rx="36" fill="#f1f1f1"/>
    </svg>
    <div class="artist-name">Hana Melrose</div>
    <div class="artist-role">Artist</div>
    <div class="contact-bar contact-bar--purple">
      <span>0432 918 246</span><span class="dot"></span>
      <span>hana@sunnydoodles.com.au</span><span class="dot"></span>
      <span>www.sunnydoodles.com.au</span>
    </div>
  </section>

  <!-- Back, version two -->
  <section class="card card--back pos-d">
    <div class="artist-name">Hana Melrose</div>
    <div class="artist-role">Artist</div>
    <div class="contact-bar contact-bar--yellow">
      <span>0432 918 246</span><span class="dot"></span>
      <span>hana@sunnydoodles.com.au</span><span class="dot"></span>
      <span>www.sunnydoodles.com.au</span>
    </div>
  </section>

</main>
</body>
</html>
```